Business cards and stationary
Venoki Imaging, llc
Professional
Miriam Colfax. Dana Pruitt
Owners
17 Harrow Lane
Bloomingburg, ny 12721 (Miriam )
52 Willowby Road
New Windsor, NY 12553 ( Dana )
Miriam 914-555-0142. /. Dana 845-555-0197
Juniper41@mailvex.com

```html
<!DOCTYPE html>
<html lang="en">
<head>
<meta charset="utf-8">
<title>Venoki Imaging, llc — Stationery</title>
<link rel="stylesheet" href="https://fonts.googleapis.com/css2?family=Montserrat:wght@400;500;600&display=swap">
<style>
  :root {
    --bg: #eef0f3;
    --paper: #ffffff;
    --navy: #1f2f6a;
    --blue: #1d5ba4;
    --blue-deep: #17458a;
    --purple: #8b2c8f;
    --grey: #6d7482;
    --faint: #eceef3;
  }
  * { box-sizing: border-box; margin: 0; padding: 0; }
  html, body { width: 1200px; height: 936px; overflow: hidden; }
  body { background: var(--bg); font-family: "Montserrat", sans-serif; color: var(--navy); }
  .canvas { position: relative; width: 1200px; height: 936px; }
  .sheet { position: absolute; background: var(--paper); box-shadow: 0 2px 8px rgba(20,30,60,.12); overflow: hidden; }
  .wave { position: absolute; left: 0; bottom: 0; width: 100%; }
  .brand { font-family: "Montserrat", sans-serif; font-weight: 500; color: var(--navy); white-space: nowrap; }
  .domain { position: absolute; width: 100%; text-align: center; color: #fff; letter-spacing: .2em; font-weight: 500; }
  .contact-list { list-style: none; font-size: 7px; color: var(--grey); line-height: 1.8; }
  .contact-list li { display: flex; align-items: center; gap: 4px; white-space: nowrap; }
  .contact-list li::before { content: ""; width: 5px; height: 5px; border-radius: 50%; background: var(--blue); flex: none; }

  /* Letterhead */
  .letterhead { left: 183px; top: 69px; width: 386px; height: 543px; }
  .letterhead .brand { position: absolute; left: 22px; top: 40px; font-size: 12px; }
  .letterhead .contact-list { position: absolute; left: 252px; top: 18px; }
  .letterhead .name-faint { position: absolute; left: 0; width: 100%; top: 244px; text-align: center; font-weight: 500; font-size: 24px; color: var(--faint); }
  .letterhead .domain { bottom: 14px; font-size: 9px; }

  /* Folder */
  .folder { left: 635px; top: 38px; width: 462px; height: 574px; }
  .folder .brand { position: absolute; left: 0; width: 100%; top: 304px; text-align: center; font-size: 24px; }
  .folder .domain { bottom: 18px; font-size: 12px; }

  /* Business cards */
  .card { left: 43px; width: 181px; height: 104px; border-radius: 5px; }
  .card-front { top: 655px; }
  .card-front .brand { position: absolute; left: 12px; top: 14px; font-size: 9px; }
  .card-front .person { position: absolute; left: 12px; top: 44px; font-size: 5.5px; color: var(--grey); line-height: 1.5; }
  .card-front .person strong { color: var(--navy); font-weight: 600; }
  .card-front .contact-list { position: absolute; left: 100px; top: 44px; font-size: 5px; }
  .card-back { top: 780px; }
  .card-back .brand { position: absolute; left: 0; width: 100%; text-align: center; top: 28px; font-size: 11px; }
  .card-back .domain { bottom: 6px; font-size: 5px; }

  /* Envelope front */
  .envelope-front { left: 246px; top: 665px; width: 458px; height: 216px; }
  .envelope-front .brand { position: absolute; left: 28px; top: 38px; font-size: 14px; }
  .envelope-front .phone { position: absolute; left: 28px; top: 64px; font-size: 6px; color: var(--grey); }

  /* Envelope back */
  .envelope-back { left: 737px; top: 665px; width: 431px; height: 216px; }
  .envelope-back .domain { top: 26px; font-size: 9px; }
</style>
</head>
<body>
<main class="canvas">

  <section class="sheet letterhead" aria-label="Letterhead">
    <div class="brand">Venoki Imaging, llc</div>
    <ul class="contact-list">
      <li>914-555-0142</li>
      <li>845-555-0197</li>
      <li>Juniper41@mailvex.com</li>
    </ul>
    <div class="name-faint">Venoki Imaging, llc</div>
    <svg class="wave" viewBox="0 0 386 70" height="70" preserveAspectRatio="none" aria-hidden="true">
      <path d="M0 14 Q190 -6 386 10 L386 70 L0 70 Z" fill="var(--purple)"/>
      <path d="M0 24 Q190 4 386 20 L386 70 L0 70 Z" fill="var(--blue)"/>
    </svg>
    <div class="domain">www.VenokiDomain.com</div>
  </section>

  <section class="sheet folder" aria-label="Presentation folder">
    <div class="brand">Venoki Imaging, llc</div>
    <svg class="wave" viewBox="0 0 462 82" height="82" preserveAspectRatio="none" aria-hidden="true">
      <path d="M0 16 Q230 -8 462 12 L462 82 L0 82 Z" fill="var(--purple)"/>
      <path d="M0 28 Q230 4 462 24 L462 82 L0 82 Z" fill="var(--blue)"/>
    </svg>
    <div class="domain">www.VenokiDomain.com</div>
  </section>

  <section class="sheet card card-front" aria-label="Business card front">
    <div class="brand">Venoki Imaging, llc</div>
    <div class="person"><strong>Miriam Colfax</strong><br><strong>Dana Pruitt</strong><br>Owners</div>
    <ul class="contact-list">
      <li>914-555-0142</li>
      <li>845-555-0197</li>
      <li>Juniper41@mailvex.com</li>
    </ul>
    <svg class="wave" viewBox="0 0 181 16" height="16" preserveAspectRatio="none" aria-hidden="true">
      <path d="M0 5 Q90 -2 181 4 L181 16 L0 16 Z" fill="var(--purple)"/>
      <path d="M0 9 Q90 2 181 8 L181 16 L0 16 Z" fill="var(--blue)"/>
    </svg>
  </section>

  <section class="sheet card card-back" aria-label="Business card back">
    <div class="brand">Venoki Imaging, llc</div>
    <svg class="wave" viewBox="0 0 181 20" height="20" preserveAspectRatio="none" aria-hidden="true">
      <path d="M0 5 Q90 -2 181 4 L181 20 L0 20 Z" fill="var(--purple)"/>
      <path d="M0 9 Q90 2 181 8 L181 20 L0 20 Z" fill="var(--blue)"/>
    </svg>
    <div class="domain">www.VenokiDomain.com</div>
  </section>

  <section class="sheet envelope-front" aria-label="Envelope front">
    <div class="brand">Venoki Imaging, llc</div>
    <div class="phone">914-555-0142</div>
  </section>

  <section class="sheet envelope-back" aria-label="Envelope back">
    <svg viewBox="0 0 431 110" width="431" height="110" preserveAspectRatio="none" aria-hidden="true" style="position:absolute;left:0;top:0">
      <defs>
        <linearGradient id="flap" x1="0" y1="0" x2="0" y2="1">
          <stop offset="0" stop-color="var(--blue)"/>
          <stop offset="1" stop-color="var(--blue-deep)"/>
        </linearGradient>
      </defs>
      <path d="M0 0 H431 V70 Q215 120 0 70 Z" fill="url(#flap)"/>
    </svg>
    <div class="domain">www.VenokiDomain.com</div>
  </section>

</main>
</body>
</html>
```